Vale Lanternwick Needs a new website!

We need a four page website for a new company based in San Francisco. We help companies connect better with their clients, employees, and vendors by implementing collaborative technology.
Similar Websites
Brindle Oarsmen - http://www.brindleoarsmen.example/
Mossquill - http://www.mossquill.example/ - I don't like the the rotating window or the pictures of people. I like the icons used to go to the next pages.
Color Combos
Blues and Yellows - http://www.huepairings.example/hue-sets/96/HueSet96.html
We prefer graphics over the actual pictures of people in the header. Pictures of people working together in the text is fine.
Web Page Layout
Index
Cloud Advisory Services
Email Everywhere
CRM Implementation
For detailed copy please see this link https://pages.fernlodge.example/a/tinkerwrensf.example/document/d/7KxTqP2mZvLw9RbHs4-_n-YcEuJdAoNfgXtVkQr5mwbe/edit
Industry/Entity Type
It Company

```html
<!DOCTYPE html>
<html lang="en">
<head>
<meta charset="utf-8">
<title>Vale Lanternwick — Collaborative Technology</title>
<link rel="stylesheet" href="https://fonts.googleapis.com/css2?family=Montserrat:wght@300;400;500;600;700&display=swap">
<style>
:root{
  --blue:#2a67b1;
  --blue-deep:#1e4f8e;
  --blue-field:#235a9e;
  --yellow:#f9bf12;
  --brown:#5a4416;
  --ink:#222;
  --grey:#555;
  --green:#3cb54a;
  --white:#fff;
}
*{margin:0;padding:0;box-sizing:border-box}
html,body{width:1200px;height:2368px;overflow:hidden}
body{position:relative;font-family:"Montserrat",sans-serif;color:var(--ink);background:var(--white)}
.abs{position:absolute}
ul{list-style:none}

/* header */
.site-header{left:0;top:0;width:1200px;height:137px;background:var(--white)}
.brand{left:76px;top:28px;display:flex;align-items:center;gap:14px}
.brand-dot{width:44px;height:44px;border-radius:50%;background:var(--yellow)}
.brand-name{font-weight:700;font-size:33px;color:var(--blue);line-height:1}
.brand-tag{left:136px;top:92px;font-size:9px;letter-spacing:1.2px;color:var(--grey);text-transform:uppercase}
.phone{left:834px;top:28px;display:flex;align-items:center;gap:12px;font-size:24px;font-weight:500;color:#333;letter-spacing:.5px}
.phone-badge{width:40px;height:40px;border-radius:50%;background:var(--green);display:flex;align-items:center;justify-content:center}
.main-nav{left:516px;top:90px;display:flex;font-size:15px;color:#333}
.main-nav li{padding:0 12px;position:relative}
.main-nav li:first-child{padding-left:0}
.main-nav li+li::before{content:"/";position:absolute;left:-4px;color:#aaa}
.main-nav .current{font-weight:500}
.main-nav .current::after{content:"";position:absolute;left:0;right:12px;top:26px;height:4px;border-radius:2px;background:var(--yellow)}

/* hero */
.hero{left:0;top:137px;width:1200px;height:560px;background:linear-gradient(120deg,#1f5fb0 0%,#2b6cc0 45%,#1c56a6 100%)}
.hero-title{left:130px;top:262px;font-size:70px;font-weight:300;color:var(--white);letter-spacing:-1px}
.hero-lede{left:130px;top:350px;width:500px;font-size:23px;font-weight:300;line-height:44px;color:var(--white)}
.hero-cta{left:130px;top:499px;width:210px;height:43px;border:2px solid var(--white);border-radius:3px;color:var(--white);font-size:21px;display:flex;align-items:center;justify-content:center}
.hero-art{left:632px;top:221px;width:521px;height:379px;border-radius:40px;background:radial-gradient(ellipse at 50% 60%,rgba(255,255,255,.28),rgba(255,255,255,.08) 70%,rgba(255,255,255,0))}

/* services */
.services{left:0;top:660px;width:1200px;height:620px;background:var(--yellow)}
.edge{left:0;width:1200px}
.section-title{left:0;width:1200px;text-align:center;font-weight:300}
.services-title{top:725px;font-size:72px;color:var(--brown)}
.services-sub{top:830px;font-size:19px;font-weight:500;color:var(--brown)}
.service{width:290px;text-align:center;color:var(--brown)}
.service-cloud{display:block;margin:0 auto}
.service h3{font-size:30px;font-weight:300;margin-top:22px;letter-spacing:-.3px}
.service p{font-size:13.5px;line-height:22px;margin-top:12px;color:#4a3a12}
.service .more{display:block;font-size:14px;font-weight:700;margin-top:14px}

/* what we do */
.work-title{top:1345px;font-size:64px;color:var(--blue)}
.work-sub{top:1433px;font-size:18px;font-weight:500;color:#222}
.step{width:180px;text-align:center;font-size:13.5px;font-weight:500;color:#222;line-height:18px}
.step svg{display:block;margin:0 auto 14px}

/* member */
.member{left:0;top:1674px;width:1200px;height:316px;background:var(--blue)}
.member-title{top:1790px;font-size:40px;color:var(--white)}
.rule{height:3px;background:rgba(255,255,255,.22);top:1818px}
.field{top:1874px;height:42px;background:var(--blue-field);border:1px solid #1a4a85;border-radius:2px;color:#d5e2f3;font-size:15px;padding:11px 26px}
.signup{left:494px;top:1952px;width:218px;height:41px;background:var(--green);color:var(--white);font-size:16px;font-weight:500;display:flex;align-items:center;justify-content:center}

/* footer */
.footer-col{top:2056px;width:178px}
.footer-col h4{font-size:19px;font-weight:400;color:#333;padding-bottom:6px;border-bottom:1px solid #bbb;margin-bottom:10px}
.footer-col li{font-size:14.5px;line-height:23px;color:#444}
.social li{display:flex;align-items:center;gap:14px;line-height:32px}
.social li::before{content:"";width:19px;height:19px;border-radius:50%;background:#333}
.legal{left:0;top:2315px;width:1200px;height:53px;background:var(--blue-deep);color:#b9c9e0;font-size:14px;padding:17px 128px}
</style>
</head>
<body>

<header class="site-header abs">
  <div class="brand abs"><span class="brand-dot"></span><span class="brand-name">Vale Lanternwick</span></div>
  <div class="brand-tag abs">Creativity. Technology. Collaboration</div>
  <div class="phone abs">
    <span class="phone-badge"><svg width="20" height="20" viewBox="0 0 20 20"><path d="M5 2h4l1 5-2.5 1.5a10 10 0 0 0 4 4L13 10l5 1v4c0 1-1 2-2 2A14 14 0 0 1 3 4c0-1 1-2 2-2z" fill="#fff"/></svg></span>
    123-555-014-270
  </div>
  <ul class="main-nav abs">
    <li class="current">Home</li>
    <li>Cloud advisory services</li>
    <li>Email Everywhere</li>
    <li>CRM Implementation</li>
  </ul>
</header>

<section class="hero abs" role="img" aria-label="Blue-tinted photograph of a server room behind the welcome message"></section>
<h1 class="hero-title abs">Wellcome to</h1>
<p class="hero-lede abs">We Help Companies Connect Better With Their Clients, Employees, And Vendors By Implementing Collaborative Technology.</p>
<div class="hero-cta abs">Contact Us</div>
<div class="hero-art abs" role="img" aria-label="Illustration of a thinking head with a gear, surrounded by business icons: clipboard, clock, light bulb, calendar, chart and target"></div>

<section class="services abs"></section>
<svg class="edge abs" style="top:628px" width="1200" height="60" viewBox="0 0 1200 60" aria-hidden="true">
  <g fill="#f9bf12">
    <ellipse cx="30" cy="48" rx="70" ry="26"/><ellipse cx="150" cy="40" rx="90" ry="32"/><ellipse cx="300" cy="44" rx="85" ry="28"/>
    <ellipse cx="450" cy="38" rx="95" ry="34"/><ellipse cx="610" cy="46" rx="80" ry="26"/><ellipse cx="760" cy="36" rx="95" ry="34"/>
    <ellipse cx="920" cy="44" rx="85" ry="28"/><ellipse cx="1060" cy="40" rx="85" ry="30"/><ellipse cx="1180" cy="46" rx="70" ry="26"/>
  </g>
</svg>
<h2 class="section-title services-title abs">Our Services</h2>
<p class="section-title services-sub abs">Lorem Ipsum Dolor Sit Amet Consectetuer Adipiscing Elit Sed Diam Nonummy Nibh</p>

<article class="service abs" style="left:127px;top:892px">
  <svg class="service-cloud" width="200" height="108" viewBox="0 0 200 108" aria-hidden="true">
    <path d="M20 100a26 26 0 0 1 10-50 36 36 0 0 1 42-26 42 42 0 0 1 74 8 34 34 0 0 1 34 34 26 26 0 0 1 0 34z" fill="#fff"/>
    <g fill="none" stroke="#6b4f14" stroke-width="3" stroke-linecap="round"><path d="M86 52a10 10 0 0 1 8-12 10 10 0 0 1 18 0 10 10 0 0 1 4 14z"/><path d="M84 66q16 8 32 0M88 74q12 6 24 0"/></g>
  </svg>
  <h3>Cloud Advisory</h3>
  <p>Forward- thinking organizations would like to be more collaborative, flexible and productive. Put your cloud program on the path to success with our Advisory Services.</p>
  <span class="more">Read More &gt;&gt;</span>
</article>

<article class="service abs" style="left:465px;top:892px">
  <svg class="service-cloud" width="200" height="108" viewBox="0 0 200 108" aria-hidden="true">
    <path d="M20 100a26 26 0 0 1 10-50 36 36 0 0 1 42-26 42 42 0 0 1 74 8 34 34 0 0 1 34 34 26 26 0 0 1 0 34z" fill="#fff"/>
    <g fill="none" stroke="#6b4f14" stroke-width="3" stroke-linejoin="round"><path d="M76 52l24-18 24 18v28H76z"/><path d="M76 52l24 16 24-16M100 62V42M93 48l7-7 7 7"/></g>
  </svg>
  <h3>Email Everywhere</h3>
  <p>Drive forward your business with innovative solutions for the enterprise with either Suiteline Apps or Deskward 365. Experience improved collaboration, security, mobility while increasing your overall IT investment.</p>
  <span class="more">Read More &gt;&gt;</span>
</article>

<article class="service abs" style="left:791px;top:892px">
  <svg class="service-cloud" width="200" height="108" viewBox="0 0 200 108" aria-hidden="true">
    <path d="M20 100a26 26 0 0 1 10-50 36 36 0 0 1 42-26 42 42 0 0 1 74 8 34 34 0 0 1 34 34 26 26 0 0 1 0 34z" fill="#fff"/>
    <g fill="none" stroke="#6b4f14" stroke-width="3"><rect x="74" y="40" width="52" height="38" rx="3"/><circle cx="88" cy="55" r="5"/><path d="M80 70q8-8 16 0M104 52h16M104 60h16M104 68h10M94 40v-5h12v5"/></g>
  </svg>
  <h3>CRM Solutions</h3>
  <p>Drive forward your business with innovative solutions for the enterprise with either Suiteline Apps or Deskward 365. Experience improved collaboration, security, mobility while increasing your overall IT investment.</p>
  <span class="more">Read More &gt;&gt;</span>
</article>

<svg class="edge abs" style="top:1220px" width="1200" height="64" viewBox="0 0 1200 64" aria-hidden="true">
  <g fill="#fff">
    <ellipse cx="40" cy="52" rx="80" ry="24"/><ellipse cx="180" cy="42" rx="100" ry="30"/><ellipse cx="350" cy="50" rx="90" ry="24"/>
    <ellipse cx="520" cy="40" rx="100" ry="30"/><ellipse cx="700" cy="48" rx="90" ry="26"/><ellipse cx="870" cy="38" rx="100" ry="30"/>
    <ellipse cx="1040" cy="48" rx="90" ry="26"/><ellipse cx="1170" cy="42" rx="80" ry="28"/><rect x="0" y="52" width="1200" height="12"/>
  </g>
</svg>

<h2 class="section-title work-title abs">What We Do</h2>
<p class="section-title work-sub abs">Lorem Ipsum Dolor Sit Amet Consectetuer Adipiscing Elit Sed Diam Nonummy Nibh</p>

<div class="step abs" style="left:159px;top:1515px">
  <svg width="60" height="60" viewBox="0 0 60 60" aria-hidden="true"><path d="M12 50l28-28 4 4-28 28-6 2z" fill="none" stroke="#2a67b1" stroke-width="4" stroke-linejoin="round"/><g stroke="#f9bf12" stroke-width="3" stroke-linecap="round"><path d="M46 8v6M52 16h6M42 14l-3-3M52 10l3-3"/></g></svg>
  Strategy
</div>
<div class="step abs" style="left:305px;top:1515px">
  <svg width="60" height="60" viewBox="0 0 60 60" aria-hidden="true"><g fill="none" stroke="#2a67b1" stroke-width="4"><rect x="10" y="40" width="8" height="12"/><rect x="24" y="32" width="8" height="20"/><rect x="38" y="24" width="8" height="28"/></g><path d="M10 30q16-24 36-22l-4-5M46 8l-5 4" fill="none" stroke="#f9bf12" stroke-width="3" stroke-linecap="round"/></svg>
  Migration
</div>
<div class="step abs" style="left:470px;top:1515px">
  <svg width="60" height="60" viewBox="0 0 60 60" aria-hidden="true"><path d="M14 26a17 17 0 0 1 30-8l4-4v12H36l5-5" fill="none" stroke="#f9bf12" stroke-width="4" stroke-linejoin="round"/><path d="M46 34a17 17 0 0 1-30 8l-4 4V34h12l-5 5" fill="none" stroke="#2a67b1" stroke-width="4" stroke-linejoin="round"/></svg>
  Implementation
</div>
<div class="step abs" style="left:639px;top:1515px">
  <svg width="60" height="60" viewBox="0 0 60 60" aria-hidden="true"><path d="M8 12h30M8 22h22M8 32h16M8 42h16M8 52h22" stroke="#2a67b1" stroke-width="4"/><circle cx="42" cy="38" r="10" fill="none" stroke="#f9bf12" stroke-width="5" stroke-dasharray="4 3"/><circle cx="42" cy="38" r="4" fill="#f9bf12"/></svg>
  Integration
</div>
<div class="step abs" style="left:830px;top:1515px">
  <svg width="60" height="60" viewBox="0 0 60 60" aria-hidden="true"><g fill="none" stroke="#2a67b1" stroke-width="3"><circle cx="30" cy="12" r="7"/><circle cx="14" cy="40" r="7"/><circle cx="46" cy="40" r="7"/></g><g fill="none" stroke="#f9bf12" stroke-width="3"><path d="M18 24l-5 6M42 24l5 6M22 52h16"/></g></svg>
  Adoption And Change<br>Management
</div>

<section class="member abs"></section>
<svg class="edge abs" style="top:1652px" width="1200" height="50" viewBox="0 0 1200 50" aria-hidden="true">
  <g fill="#fff">
    <rect x="0" y="0" width="1200" height="14"/>
    <ellipse cx="40" cy="14" rx="80" ry="24"/><ellipse cx="200" cy="18" rx="100" ry="26"/><ellipse cx="380" cy="12" rx="90" ry="24"/>
    <ellipse cx="560" cy="18" rx="100" ry="26"/><ellipse cx="740" cy="12" rx="90" ry="24"/><ellipse cx="910" cy="18" rx="100" ry="26"/>
    <ellipse cx="1080" cy="14" rx="90" ry="24"/><ellipse cx="1190" cy="18" rx="70" ry="22"/>
  </g>
</svg>
<h2 class="section-title member-title abs">Become A Member</h2>
<div class="rule abs" style="left:128px;width:280px"></div>
<div class="rule abs" style="left:805px;width:278px"></div>
<div class="field abs" style="left:123px;width:308px">Name</div>
<div class="field abs" style="left:450px;width:306px">Email Adderess</div>
<div class="field abs" style="left:775px;width:308px">Contact Number</div>
<div class="signup abs">Signup Now</div>

<footer>
  <div class="footer-col abs" style="left:128px">
    <h4>Important Links</h4>
    <ul><li>Home</li><li>Dedicated<br>Servers</li><li>&nbsp;VPS<br>hosting</li><li>&nbsp;Shared<br>Hosting</li><li>Company</li></ul>
  </div>
  <div class="footer-col abs" style="left:385px">
    <h4>FAQ</h4>
    <ul><li>Help</li><li>Privacy Policy</li><li>Terms of<br>Service</li><li>Contact Us</li><li>Insights</li><li>Meet the team</li></ul>
  </div>
  <div class="footer-col abs" style="left:644px">
    <h4>About</h4>
    <ul><li>What we do</li><li>Insights</li><li>Meet the<br>team</li><li>Careers</li><li>Our story</li><li>Media</li></ul>
  </div>
  <div class="footer-col abs" style="left:903px">
    <h4>Social Media</h4>
    <ul class="social"><li>Friendwall</li><li>Careerlink</li><li>Chirpline</li><li>Clipstream</li><li>Circleplus</li></ul>
  </div>
  <div class="legal abs">© Copyright 2014 Vale-Lanternwick All Rights Reserved.</div>
</footer>

</body>
</html>
```